Kestrel Volt Electrical Pty Ltd (Flyer)

INSTRUCTIONS:
we need a promotional flyer that is short and sweet and to the point for letter box drop (has to be eye catching).
we want the flyer to be double sided A4 sized and foldable into 3 sections (i have uploaded a hand drawn A ROUGH flyer just as an idea of what we are after ,see uploads)
-the front of the flyer will be divided into 3 parts folded and the back will be A4 letter style.
MUST HAVE'S!
-must have logo, email address and contact number 1300 517 903 (have uploaded)
-must state where contact number is "one call for all"
-must have "Energy, Efficiency, Solution's" stated somewhere
-must have services we offer
-must have Lic number 7315098K
-Must have all content listed in brief.
SEE BELOW BRIEF (i have uploaded a rough drawn template)
Front page (folded into 3 parts)
Part 1 -
-logo
-website
-must state "Electricians and technicians" and also "Australian owned and operated"
Part 2 -
- bullet point heading #Energy (in red) #Efficiency (in green) #solutions (in blue)
-Must state "SAVE 60% OFF YOUR ELECTRICITY BILL"
-Must state "One call for ALL Electrical and technical needs 1300 517 930"
Part 3 - (promotional offer)
(photo of torvane L.E.D light, i have uploaded)
- must state "promotional offer" supply/install 13 Watt L.E.D downlights @ $50.00 + GSTper fitting
-3 year warranty
-Dimmable
-Minimum 4 fittings
CALL NOW 1300 517 903
INSIDE OF FLYER
(set out in A4 letter format)
Top of page:
-logo
-Must state -"save up to 60% on electricity costs"
-Must state - call for assessment 1300 517 903 or visit website Kestrelvolt.com.au
Underneath above information on inside of flyer:
ENERGY … EFFICIENCY … SOLUTIONS
ABOUT US:
Kestrel Volt Electrical Pty Ltd is a progressive electrical company in Sydney offering expertise in the reinvention of homes and offices for a more energy efficient and economical outcome. Our work is informed by a sound knowledge of the latest product design and availability in lighting and energy efficient products including hot water, air conditioning and solar power.
We offer “one call for all your electrical needs” and deliver prompt and reliable service at a competitive price all over the Sydney CBD and Greater Sydney area.
SERVICES:
We offer a variety of services in the electrical and communications fields
• All lighting and power needs
• House rewires
• Switchboard upgrades and relocations
• Commercial fit outs
• Air Conditioning
• Data / Phone / TV installations
• All Builders work (including Owner / Builders)
ENERGY, EFFICIENCY, SOLUTIONS
• LED lighting refits to existing homes and offices
• Solar Hot Water Systems
• Electricity regeneration (Solar Power)
• Inverter Air Conditioning Systems
• Time in use metering (how it benefits you)
Note:
please look at uploads for rough idea.
Updates
Flyer must be double sided (see breif)
Hi Guys,
HI GUYS
Hi Guys,
Reason: I have changed the deadline please submite both sides of the flyer
thank you
Air Conditioning

```html
<!DOCTYPE html>
<html lang="en">
<head>
<meta charset="utf-8">
<title>Kestrel Volt Electrical – Flyer</title>
<link rel="stylesheet" href="https://fonts.googleapis.com/css2?family=Ubuntu:wght@400;500;700&family=Crimson+Text:wght@400;600&family=Tinos:wght@400;700&display=swap">
<style>
  :root{
    --stage:#e6e3de;
    --paper:#f4f4f4;
    --ink:#1c1c1c;
    --grey:#4d4d4d;
    --arrow-grey:#9d9d9d;
    --rule-grey:#c9c9c9;
    --red:#e0262b;
    --green:#3aaa35;
    --blue:#1ea7df;
    --sans:"Ubuntu", Arial, sans-serif;
    --serif:"Crimson Text", Georgia, serif;
    --figures:"Tinos", "Times New Roman", serif;
  }
  *{margin:0;padding:0;box-sizing:border-box}
  html,body{width:1200px;height:770px;overflow:hidden;background:var(--stage)}
  .canvas{position:relative;width:1200px;height:770px}
  .page{position:absolute;top:34px;width:540px;height:698px;overflow:hidden;
        background:linear-gradient(180deg,#ffffff 0%,var(--paper) 55%,#e9e9e9 100%);
        box-shadow:0 2px 8px rgba(0,0,0,.25)}
  .page--front{left:44px}
  .page--inside{left:621px}
  .abs{position:absolute;white-space:nowrap}
  .center{left:0;right:0;text-align:center}

  /* brand */
  .brand-name{font-family:var(--sans);font-weight:700;color:var(--ink);letter-spacing:-.5px;line-height:1}
  .brand-sub{font-family:var(--sans);font-weight:700;color:var(--ink);letter-spacing:6px;line-height:1}
  .brand-tagline{font-family:var(--serif);font-style:italic;color:var(--ink);line-height:1}
  .web{font-family:var(--sans);font-weight:700;color:var(--ink);line-height:1}

  /* front */
  .lic{font-family:var(--sans);font-size:8px;color:var(--ink);top:12px;left:334px}
  .front-phone-small{font-family:var(--sans);font-size:10px;color:var(--ink);top:135px}
  .owned{font-family:var(--sans);font-weight:700;font-size:15px;color:var(--grey);top:192px}
  .headline{font-family:var(--sans);font-weight:500;color:var(--green)}
  .quoted{line-height:34px;height:34px}
  .quote{font-family:var(--figures);font-weight:700;color:var(--red);position:relative;display:inline-block;line-height:1}
  .quote--open{top:-4px;margin-right:2px}
  .quote--close{top:10px;margin-left:2px}
  .assess{font-family:var(--serif);font-size:20px;line-height:24px;color:var(--ink);top:291px}
  .pillars{font-family:var(--serif);font-size:24px;line-height:1.2}
  .pillars span{margin:0 6px}
  .c-red{color:var(--red)} .c-green{color:var(--green)} .c-blue{color:var(--blue)}
  .one-call{font-family:var(--serif);font-size:27px;color:var(--ink);top:360px}
  .needs{font-family:var(--serif);font-size:12px;color:var(--ink);top:398px}
  .big-phone{font-family:var(--figures);color:var(--red);line-height:1}
  .product-frame{position:absolute;left:64px;top:507px;width:114px;height:131px;border:1px solid #333;background:#fff}
  .offer-lines{font-family:var(--sans);color:var(--ink)}
  .offer-bullets{list-style:none;font-family:var(--sans);font-size:17px;line-height:21px}
  .offer-bullets li::before{content:"•";margin-right:5px}
  .call-now{font-family:var(--figures);font-weight:700;font-size:36px;color:var(--blue);left:64px;top:650px;letter-spacing:.5px}

  /* inside */
  .divider{position:absolute;left:202px;top:50px;width:2px;height:108px;background:var(--blue)}
  .inside-head{font-family:var(--sans);font-weight:500;font-size:23px;line-height:1;color:var(--green);left:214px;top:67px}
  .call-assess{font-family:var(--serif);font-size:21px;line-height:1;letter-spacing:1.5px;color:var(--ink);left:214px;top:97px}
  .inside-phone{left:214px;top:126px;font-size:23px}
  .inside-web{left:372px;top:132px;font-size:12px}
  .section-title{font-family:var(--serif);font-size:14px;letter-spacing:1px;left:18px}
  .body-copy{position:absolute;left:18px;width:504px;font-family:var(--serif);font-size:11.6px;line-height:16.8px;letter-spacing:.45px;color:var(--ink);text-align:justify}
  .service-list{position:absolute;left:18px;list-style:none;font-family:var(--serif);font-size:11.6px;line-height:16px;letter-spacing:.5px;color:var(--ink)}
  .service-list li::before{content:"•";color:var(--red);margin-right:6px}
</style>
</head>
<body>
<div class="canvas">

  <section class="page page--front">
    <div class="abs lic">LicNo: 7315098K</div>

    <div class="abs center brand-name" style="top:62px;font-size:34px">Kestrel Volt</div>
    <div class="abs center brand-sub" style="top:99px;font-size:17px">Electrical</div>
    <div class="abs center brand-tagline" style="top:118px;font-size:13px">“Electricians &amp; Technicians”</div>
    <div class="abs center front-phone-small">1300 517 903</div>
    <div class="abs center web" style="top:155px;font-size:12px">www.Kestrelvolt.com.au</div>

    <div class="abs center owned">Austrailan owned + Operated</div>

    <svg class="abs" style="left:0;top:196px" width="540" height="80" viewBox="0 0 540 80" aria-hidden="true">
      <rect x="56" y="29" width="440" height="18" fill="var(--arrow-grey)"/>
      <polygon points="0,38 58,6 58,70" fill="var(--arrow-grey)"/>
      <circle cx="502" cy="38" r="38" fill="var(--green)"/>
    </svg>

    <div class="abs center quoted" style="top:252px">
      <span class="quote quote--open" style="font-size:40px">“</span><span class="headline" style="font-size:29px">Save 60% on Electricity</span><span class="quote quote--close" style="font-size:40px">”</span>
    </div>
    <div class="abs center assess">— Have your&nbsp; home assesed —</div>
    <div class="abs center pillars" style="top:323px">
      <span class="c-red">• Energy</span><span class="c-green">•Efficency</span><span class="c-blue">•Solutions</span>
    </div>
    <div class="abs center one-call">‘One call for all’</div>
    <div class="abs center needs">Electrical Technical Needs</div>
    <div class="abs center big-phone" style="top:418px;font-size:33px">1300 517 903</div>

    <svg class="abs" style="left:0;top:426px" width="540" height="80" viewBox="0 0 540 80" aria-hidden="true">
      <rect x="40" y="29" width="445" height="18" fill="var(--arrow-grey)"/>
      <polygon points="540,38 482,6 482,70" fill="var(--arrow-grey)"/>
      <circle cx="38" cy="38" r="38" fill="var(--red)"/>
    </svg>

    <div class="product-frame">
      <div role="img" aria-label="Photo of a white recessed 13 watt LED downlight" style="position:absolute;left:18px;top:36px;width:78px;height:44px;border-radius:50%;background:radial-gradient(ellipse at 50% 40%,#ffffff 0%,#e4e6e8 60%,#b9bcc0 100%)"></div>
      <svg style="position:absolute;left:14px;top:92px" width="88" height="32" viewBox="0 0 88 32" aria-hidden="true">
        <circle cx="16" cy="16" r="14" fill="#8cc63f"/>
        <rect x="50" y="5" width="32" height="22" rx="4" fill="#d7262e"/>
      </svg>
    </div>

    <div class="abs quoted" style="left:246px;top:494px">
      <span class="quote quote--open" style="font-size:34px">“</span><span class="headline" style="font-size:29px">Promotional Offer</span><span class="quote quote--close" style="font-size:34px">”</span>
    </div>
    <div class="abs offer-lines" style="left:251px;top:531px;font-size:19px">Supply Install - 13 Watt LED D/LT</div>
    <div class="abs offer-lines" style="left:251px;top:555px;font-size:17px">@ $50 Per Fitting</div>
    <ul class="abs offer-bullets" style="left:251px;top:580px">
      <li class="c-red">3 Year Warranty</li>
      <li class="c-green">Dimmable</li>
      <li class="c-blue">Min 4 Fittings</li>
    </ul>

    <div class="abs call-now">Call Us Now&nbsp; 1300 517 903</div>
  </section>

  <section class="page page--inside">
    <svg class="abs" style="left:0;top:0" width="540" height="698" viewBox="0 0 540 698" aria-hidden="true">
      <rect x="0" y="6" width="470" height="6" fill="var(--rule-grey)"/>
      <polygon points="0,0 60,0 60,32" fill="var(--arrow-grey)"/>
      <circle cx="502" cy="-2" r="38" fill="var(--green)"/>
      <rect x="60" y="688" width="440" height="6" fill="var(--rule-grey)"/>
      <polygon points="483,666 539,698 483,698" fill="var(--arrow-grey)"/>
      <circle cx="38" cy="698" r="38" fill="var(--red)"/>
      <polygon points="203,40 198,52 208,52" fill="var(--blue)"/>
    </svg>

    <div class="abs brand-name" style="left:18px;top:82px;font-size:30px">Kestrel Volt</div>
    <div class="abs brand-sub" style="left:19px;top:116px;font-size:16px">Electrical</div>
    <div class="abs brand-tagline" style="left:22px;top:136px;font-size:13px">“Electricians &amp; Technicians”</div>
    <div class="divider"></div>

    <div class="abs inside-head">Save 60% on Electricity Costs</div>
    <div class="abs call-assess">Call for assesment</div>
    <div class="abs big-phone inside-phone">1300 517 903</div>
    <div class="abs web inside-web">www.Kestrelvolt.com.au</div>

    <div class="abs pillars c-red" style="left:81px;top:176px;font-size:25px">• Energy</div>
    <div class="abs pillars c-green" style="left:213px;top:176px;font-size:25px">•Efficency</div>
    <div class="abs pillars c-blue" style="left:355px;top:176px;font-size:25px">•Solutions</div>

    <div class="abs section-title c-red" style="top:240px">ABOUT US</div>
    <p class="body-copy" style="top:259px">We are a progressive electrical company in Sydney offering expertise in the reinvention of homes and offices for a more energy efficient and economical outcome. Our work is informed by a sound knowledge of the latest product design and availability in lighting and energy efficient products including hot water, air conditioning and solar power. We offer “one call for all your electrical needs” and deliver prompt and reliable service at a competitive price all over the Sydney CBD and Greater Sydney area.</p>

    <div class="abs section-title c-green" style="top:373px">SERVICES</div>
    <p class="body-copy" style="top:393px">We offer a variety of services in the electrical and communications fields.</p>
    <ul class="service-list" style="top:413px">
      <li>All lighting and power needs</li>
      <li>House rewires</li>
      <li>Switchboard upgrades and relocations</li>
      <li>Commercial fit outs</li>
      <li>Air Conditioning</li>
      <li>Data / Phone / TV installations</li>
      <li>All Builders work (including Owner / Builders)</li>
    </ul>

    <div class="abs section-title" style="top:535px;font-size:13px"><span class="c-red">ENERGY,</span> <span class="c-green">EFFICIENCY,</span> <span class="c-blue">SOLUTIONS</span></div>
    <ul class="service-list" style="top:553px">
      <li>LED lighting refits to existing homes and offices</li>
      <li>Solar Hot Water Systems</li>
      <li>Electricity regeneration (Solar Power)</li>
      <li>Inverter Air Conditioning Systems</li>
      <li>Time in use metering (how it benefits you)</li>
    </ul>
  </section>

</div>
</body>
</html>
```